Global Expert Network Firm needs business card design

We need business card design for a new company based in Seoul, South Korea called 'Corwell Insight Partners'. We recruit industry experts covering all countries and connect our client and recruited expert by phone, face-to-face meetings and etc. We are a global expert network firm that is focused on delivering high-quality experts to our clients throughout the world. Our clients include multinational corporations, global consulting firms, private equity firms, venture capital firms, asset management companies.
We have made new logo and please find attachment.(Please use new logo)
Target Market(s)
Global Consulting Firms, Investment Firms, Private Equity Firms, Venture Capital Firms.
Industry/Entity Type
Recruitment
Contact Information for Business Card
We need two Languages (English and Korean Version).
The front is Korean and the back is English version.
[The back] [English]
Company Name: Corwell Insight Partners, Inc.
CEO Name: Daniel Park
Address: #507, Hanbit Bldg, 82 Maebongsan-ro, Dobong-gu, Seoul, 01327, Korea
Tel. +82 2 718 4052
Fax. +82 2 864 1097
Mobile. +82 10 7264 8815
Email: daniel@corwellip.com
Web: www.corwellip.com
[The front] [Korean] => Described in same order as English version.
회사명: 코웰인사이트파트너스(주)
대표이사: 박도현
주소: 서울시 도봉구 매봉산로 82 한빛빌딩 507호
Tel. 02 718 4052
Fax. 02 864 1097
Mobile. 010 7264 8815
Web: www.corwellip.com
Look and feel
Each slider illustrates characteristics of the customer's brand and the style your logo design should communicate.

```html
<!DOCTYPE html>
<html lang="en">
<head>
<meta charset="utf-8">
<title>Corwell Insight Partners — Business Cards</title>
<link rel="stylesheet" href="https://fonts.googleapis.com/css2?family=Arimo:wght@400;700&family=Nanum+Myeongjo:wght@400;700&display=swap">
<style>
  :root {
    --backdrop: #2b2c30;
    --card: #f7f7f7;
    --navy: #1f2456;
    --ink: #6b6b6b;
    --rule: #8a8a8a;
  }
  * { margin: 0; padding: 0; box-sizing: border-box; }
  html, body { width: 1200px; height: 1200px; overflow: hidden; }
  body {
    background: var(--backdrop);
    font-family: "Arimo", Arial, sans-serif;
    position: relative;
  }
  .card {
    position: absolute;
    left: 240px;
    width: 720px;
    height: 412px;
    background: var(--card);
    color: var(--ink);
  }
  .card--english { top: 150px; }
  .card--korean { top: 640px; }

  .brand {
    position: absolute;
    top: 42px;
    right: 54px;
    display: flex;
    align-items: center;
    gap: 12px;
  }
  .brand__square { width: 34px; height: 34px; background: var(--navy); }
  .brand__name {
    color: var(--navy);
    font-size: 17px;
    font-weight: 400;
    letter-spacing: 0.06em;
    text-transform: uppercase;
    line-height: 1.25;
    text-align: right;
  }

  .person { position: absolute; left: 54px; top: 212px; }
  .person__name { color: var(--navy); font-size: 22px; font-weight: 700; line-height: 1.1; }
  .person__title { font-size: 16px; line-height: 1.2; }
  .card--korean .person { top: 200px; }
  .card--korean .person__name { font-family: "Nanum Myeongjo", serif; font-size: 28px; font-weight: 700; }
  .card--korean .person__title { font-family: "Nanum Myeongjo", serif; font-size: 16px; letter-spacing: 0.04em; }

  .divider {
    position: absolute;
    left: 54px; right: 56px; top: 270px;
    border-top: 1.5px solid var(--rule);
  }

  .details {
    position: absolute;
    left: 54px; top: 290px;
    font-size: 15.5px;
    line-height: 21px;
  }
  .details__address--korean { font-family: "Nanum Myeongjo", serif; font-size: 16px; letter-spacing: 0.02em; }
  .contact-row { display: flex; gap: 20px; margin-top: 6px; }
  .contact { display: flex; align-items: center; gap: 4px; }
  .contact svg { width: 13px; height: 13px; fill: var(--navy); }
  .web { color: var(--navy); }
</style>
</head>
<body>

<section class="card card--english" aria-label="English side">
  <div class="brand">
    <div class="brand__name">Corwell Insight<br>Partners</div>
    <div class="brand__square"></div>
  </div>
  <div class="person">
    <p class="person__name">Daniel Park</p>
    <p class="person__title">CEO</p>
  </div>
  <div class="divider"></div>
  <div class="details">
    <p>#507, Hanbit Bldg, 82 Maebongsan-ro, Dobong-gu<br>Seoul, 01327, Korea</p>
    <div class="contact-row">
      <span class="contact"><svg viewBox="0 0 16 16"><path d="M3 1l3 3-2 2c1 2 3 4 5 5l2-2 3 3-2 2C6 14 2 10 1 3z"/></svg>+82 2 718 4052</span>
      <span class="contact"><svg viewBox="0 0 16 16"><path d="M4 1h8v4H4zM1 6h14v6h-3v3H4v-3H1zM5 10v3h6v-3z"/></svg>+82 2 864 1097</span>
      <span class="contact"><svg viewBox="0 0 16 16"><path d="M4 0h8v16H4zM5.5 1.5v11h5v-11z"/></svg>+82 10 7264 8815</span>
    </div>
    <p>daniel@corwellip.com | <span class="web">www.corwellip.com</span></p>
  </div>
</section>

<section class="card card--korean" lang="ko" aria-label="Korean side">
  <div class="brand">
    <div class="brand__name">Corwell Insight<br>Partners</div>
    <div class="brand__square"></div>
  </div>
  <div class="person">
    <p class="person__name">박도현</p>
    <p class="person__title">대표이사</p>
  </div>
  <div class="divider"></div>
  <div class="details">
    <p class="details__address--korean">코웰인사이트파트너스(주), 서울시 도봉구 매봉산로 82 한빛빌딩 507호</p>
    <div class="contact-row">
      <span class="contact"><svg viewBox="0 0 16 16"><path d="M3 1l3 3-2 2c1 2 3 4 5 5l2-2 3 3-2 2C6 14 2 10 1 3z"/></svg>+82 2 718 4052</span>
      <span class="contact"><svg viewBox="0 0 16 16"><path d="M4 1h8v4H4zM1 6h14v6h-3v3H4v-3H1zM5 10v3h6v-3z"/></svg>+82 2 864 1097</span>
      <span class="contact"><svg viewBox="0 0 16 16"><path d="M4 0h8v16H4zM5.5 1.5v11h5v-11z"/></svg>+82 10 7264 8815</span>
    </div>
    <p>daniel@corwellip.com | <span class="web">www.corwellip.com</span></p>
  </div>
</section>

</body>
</html>
```